Business card for medical clinic

I need an upmarket, modern medical/health business card for my clinic

Contact Information for Business Card

name, address, email, qr code

```html
<!DOCTYPE html>
<html lang="en">
<head>
<meta charset="utf-8">
<title>Calder Health Partners – Business Card</title>
<link rel="stylesheet" href="https://fonts.googleapis.com/css2?family=Cinzel:wght@400;600&family=Arimo:wght@400&display=swap">
<style>
  :root {
    --stage: #3d3d3d;
    --white: #ffffff;
    --navy: #1c2b4f;
    --deep: #12416f;
    --bright: #00a8e6;
    --mid: #1673b3;
    --logo-blue: #1b6fb0;
    --name-navy: #1d3a6a;
    --grey: #9a9a9a;
    --back-logo: #22b4e6;
  }
  * { margin: 0; padding: 0; box-sizing: border-box; }
  html, body { width: 1200px; height: 803px; overflow: hidden; background: var(--stage); }
  .canvas { position: relative; width: 1200px; height: 803px; }

  .card {
    position: absolute;
    width: 525px;
    height: 300px;
    border-radius: 18px;
    overflow: hidden;
    box-shadow: 0 10px 24px rgba(0,0,0,0.35);
  }
  .card--front { left: 50px; top: 110px; background: var(--white); }
  .card--back {
    left: 625px; top: 393px;
    background: radial-gradient(ellipse 60% 75% at 45% 45%, var(--bright) 0%, var(--mid) 35%, var(--deep) 65%, var(--navy) 100%);
  }

  .front-swoosh { position: absolute; inset: 0; width: 525px; height: 300px; }

  .holder {
    position: absolute;
    right: 200px;
    top: 30px;
    text-align: right;
  }
  .holder__name {
    font-family: "Cinzel", serif;
    font-weight: 600;
    font-size: 22px;
    letter-spacing: 1px;
    color: var(--name-navy);
  }
  .holder__title {
    font-family: "Arimo", sans-serif;
    font-size: 11px;
    color: var(--grey);
    margin-top: 2px;
  }

  .contact {
    position: absolute;
    right: 20px;
    top: 66px;
    list-style: none;
    font-family: "Arimo", sans-serif;
    font-size: 11.5px;
    color: var(--white);
    text-align: right;
    line-height: 1.55;
  }
  .contact__row { display: flex; justify-content: flex-end; align-items: center; gap: 7px; }
  .contact__icon { width: 11px; height: 11px; flex: none; }
  .contact__address { margin-top: 8px; padding-right: 18px; }

  .brand {
    position: absolute;
    display: flex;
    align-items: center;
    gap: 8px;
  }
  .brand--front { left: 28px; top: 128px; }
  .brand--back { left: 92px; top: 126px; }
  .brand__dot { border-radius: 50%; flex: none; }
  .brand--front .brand__dot { width: 13px; height: 13px; background: var(--logo-blue); }
  .brand--back .brand__dot { width: 20px; height: 20px; background: var(--back-logo); }
  .brand__name {
    font-family: "Cinzel", serif;
    font-weight: 400;
    white-space: nowrap;
  }
  .brand--front .brand__name { font-size: 16px; letter-spacing: 1px; color: var(--logo-blue); }
  .brand--back .brand__name { font-size: 25px; letter-spacing: 1.5px; color: var(--back-logo); }
</style>
</head>
<body>
<main class="canvas">

  <section class="card card--front" aria-label="Card front">
    <svg class="front-swoosh" viewBox="0 0 525 300" aria-hidden="true">
      <defs>
        <radialGradient id="swooshFill" cx="0.55" cy="0.55" r="0.7">
          <stop offset="0" stop-color="#00a8e6"/>
          <stop offset="0.4" stop-color="#1673b3"/>
          <stop offset="0.75" stop-color="#12416f"/>
          <stop offset="1" stop-color="#1c2b4f"/>
        </radialGradient>
      </defs>
      <path d="M372 0 C 392 120 300 225 0 238 L0 300 L525 300 L525 0 Z" fill="url(#swooshFill)"/>
      <path d="M362 0 C 380 120 290 218 0 230" fill="none" stroke="#1673b3" stroke-width="2.5"/>
      <path d="M354 0 C 370 118 282 212 0 224" fill="none" stroke="#5fb8e6" stroke-width="0.8"/>
    </svg>

    <div class="holder">
      <p class="holder__name">Daniel Reyes</p>
      <p class="holder__title">President</p>
    </div>

    <ul class="contact">
      <li class="contact__row">555-210-4830
        <svg class="contact__icon" viewBox="0 0 12 12" aria-hidden="true"><path d="M3 1 L5 3.5 L4 4.8 C4.8 6.4 5.8 7.3 7.2 8 L8.5 7 L11 9 L9.6 11 C5.5 10.6 1.4 6.5 1 2.4 Z" fill="#fff"/></svg>
      </li>
      <li class="contact__row">555-210-4831
        <svg class="contact__icon" viewBox="0 0 12 12" aria-hidden="true"><rect x="3" y="0.5" width="6" height="11" rx="1" fill="none" stroke="#fff"/><circle cx="6" cy="9.6" r="0.7" fill="#fff"/></svg>
      </li>
      <li class="contact__row">hello@caldercare.com
        <svg class="contact__icon" viewBox="0 0 12 12" aria-hidden="true"><rect x="0.5" y="2.5" width="11" height="7" fill="#fff"/><path d="M0.5 2.5 L6 6.5 L11.5 2.5" fill="none" stroke="#1c4f86"/></svg>
      </li>
      <li class="contact__row">www.caldercare.com
        <svg class="contact__icon" viewBox="0 0 12 12" aria-hidden="true"><circle cx="6" cy="6" r="5.2" fill="none" stroke="#fff"/><ellipse cx="6" cy="6" rx="2.2" ry="5.2" fill="none" stroke="#fff" stroke-width="0.8"/><path d="M0.8 6 H11.2" stroke="#fff" stroke-width="0.8"/></svg>
      </li>
      <li class="contact__address">412 Willow Crest Road<br>Brookfield, Canada 20915</li>
    </ul>

    <div class="brand brand--front">
      <span class="brand__dot"></span>
      <span class="brand__name">Calder Health Partners</span>
    </div>
  </section>

  <section class="card card--back" aria-label="Card back">
    <div class="brand brand--back">
      <span class="brand__dot"></span>
      <span class="brand__name">Calder Health Partners</span>
    </div>
  </section>

</main>
</body>
</html>
```